PowerPoint design MervoSan

We need a PowerPoint set-up based upon our existing logo (see joint file)
Our company is operating in the health care and life science sector. We are mainly focussing on international business

Target Market(s)

International

Industry/Entity Type

health care and life sciences

Requirements
Must have
• Logos as added

```html
<!DOCTYPE html>
<html lang="en">
<head>
<meta charset="utf-8">
<title>MervoSan – Presentation Set-up</title>
<link href="https://fonts.googleapis.com/css2?family=Roboto:wght@700;900&family=Open+Sans:wght@300;400;600;700&display=swap" rel="stylesheet">
<style>
:root{
  --stage:#d9d8da;
  --paper:#ffffff;
  --navy:#0d4a8b;
  --green:#5bbc17;
  --orange:#f39c0a;
  --red:#e0335a;
  --dark:#1f2833;
  --ink:#3a3a3a;
  --grey:#6e6e6e;
  --soft:#9a9a9a;
  --faint:#f1f1f1;
  --head:'Roboto',sans-serif;
  --body:'Open Sans',sans-serif;
}
*{margin:0;padding:0;box-sizing:border-box}
html,body{width:1200px;height:696px;overflow:hidden;background:var(--stage);font-family:var(--body);color:var(--ink)}
.canvas{position:relative;width:1200px;height:696px}
.slide{position:absolute;background:var(--paper);overflow:hidden;box-shadow:0 1px 3px rgba(0,0,0,.18)}
.slide.dark{background:var(--dark);color:#fff}
.abs{position:absolute}
.head{font-family:var(--head);font-weight:700;letter-spacing:-.04em;line-height:1}
.brand{position:absolute;display:flex;align-items:center;gap:5px}
.brand .dot{border-radius:50%;background:var(--navy)}
.brand .name{font-family:var(--body);font-weight:600;color:var(--navy);line-height:1}
.ring{position:absolute;border-radius:50%}
.footer{position:absolute;display:flex;height:100%}
.lorem{font-size:4px;line-height:5.4px;color:var(--grey)}
.photo{position:absolute}

/* Slide: vision / mission / result */
.s-vmr{left:19px;top:18px;width:768px;height:432px}
.s-vmr .title{left:33px;top:32px;font-size:31px;color:var(--ink)}
.s-vmr .sub{left:33px;top:86px;font-size:12px;color:var(--green);font-weight:300}
.pillar{position:absolute;top:160px;width:170px;text-align:center}
.pillar svg{display:block;margin:0 auto;height:44px}
.pillar .bar{width:82px;height:3px;margin:19px auto 0}
.pillar h3{font-family:var(--head);font-weight:900;font-size:16px;letter-spacing:-.04em;margin-top:28px}
.pillar p{font-size:10.2px;line-height:13.5px;color:var(--grey);margin-top:12px;font-weight:300}
.vmr-foot{position:absolute;left:619px;top:400px;height:18px;width:130px}
.vmr-foot .url{background:var(--dark);width:103px;height:18px;transform:skewX(-14deg);display:flex;align-items:center;justify-content:center}
.vmr-foot .url span{transform:skewX(14deg);font-size:6.6px;color:#fff}
.vmr-foot .pg{background:var(--green);width:27px;height:18px;transform:skewX(-14deg);display:flex;align-items:center;justify-content:center;color:#fff;font-size:6.6px}
.vmr-foot .pg span{transform:skewX(14deg)}

/* Slide: strategy */
.s-strat{left:804px;top:18px;width:379px;height:212px}
.s-strat .t{left:14px;top:107px;font-size:18.5px;line-height:20.5px;color:var(--ink)}
.s-strat .t span{color:var(--green)}
.s-strat .sub{left:14px;top:168px;font-size:5.6px;color:var(--grey)}
.s-strat .note{left:12px;top:178px;width:120px;height:20px;background:var(--soft);color:#fff;font-size:3.8px;line-height:5px;padding:2px 3px}
.s-strat .card{left:148px;top:117px;width:104px;height:81px;background:var(--green);color:#fff;padding:9px 11px}
.s-strat .card h4{font-size:6px;font-weight:700;margin-bottom:6px}
.s-strat .card p{font-size:3.8px;line-height:5px;margin-bottom:4px}
.s-strat .panel{left:252px;top:0;width:127px;height:198px;background:var(--dark)}
.feat{position:absolute;left:22px;width:100px;display:flex;gap:8px;color:#fff}
.feat svg{flex:none;width:12px;height:14px;margin-top:2px}
.feat h5{font-size:5.2px;font-weight:700;margin-bottom:1px}
.feat p{font-size:3.8px;line-height:5px}

/* Slide: figures */
.s-fig{left:803px;top:239px;width:380px;height:213px}
.s-fig .title{right:143px;top:43px;font-size:16px;color:var(--ink)}
.s-fig .sub{right:143px;top:61px;font-size:5.6px;color:var(--grey)}
.stat{position:absolute;top:88px;width:64px}
.stat .box{height:51px;color:#fff;text-align:center;padding-top:11px}
.stat .box b{display:block;font-size:12px;font-weight:700}
.stat .box small{display:block;font-size:5px;line-height:6px;margin-top:5px}
.stat p{font-size:3.8px;line-height:5.6px;color:var(--grey);margin-top:4px;padding-left:1px}
.s-fig .panel{left:251px;top:117px;width:105px;height:81px;background:var(--dark);color:#fff}
.s-fig .big{left:37px;top:13px;font-size:10px;font-weight:700}
.s-fig .res{left:36px;top:23px;font-size:7.4px;color:var(--green)}
.s-fig .rule{left:10px;top:38px;width:87px;height:1px;background:rgba(255,255,255,.5)}
.s-fig .ptext{left:12px;top:44px;width:84px;font-size:3.8px;line-height:5.4px}

/* Slide: what we do */
.s-do{left:18px;top:464px;width:377px;height:212px}
.s-do .box{left:20px;top:94px;width:110px;height:30px;background:var(--paper)}
.s-do .title{left:0;width:110px;text-align:center;top:6px;font-size:15px;color:var(--ink)}
.s-do .sub{left:0;width:110px;text-align:center;top:23px;font-size:5.2px;color:var(--green)}
.s-do .body{left:24px;top:128px;width:102px;text-align:justify}
.service{position:absolute;top:96px;width:64px}
.service .c{width:30px;height:30px;border-radius:50%;margin-left:0;display:flex;align-items:center;justify-content:center}
.service .c svg{width:15px;height:15px}
.service h6{font-size:5.8px;font-weight:700;color:var(--ink);margin-top:9px}
.service p{margin-top:4px;font-size:3.8px;line-height:5.2px;color:var(--grey)}
.do-foot{position:absolute;left:305px;top:197px;height:8px;display:flex}
.do-foot .url{width:58px;height:8px;background:var(--dark);transform:skewX(-14deg);color:#fff;font-size:3.2px;display:flex;align-items:center;justify-content:center}
.do-foot .pg{width:13px;height:8px;background:var(--green);transform:skewX(-14deg);color:#fff;font-size:3.2px;display:flex;align-items:center;justify-content:center}

/* Slides: timelines */
.s-time{left:408px;top:463px;width:379px;height:213px}
.s-end{left:803px;top:463px;width:380px;height:213px}
.tl-title{font-family:var(--head);font-weight:700;font-size:15.5px;letter-spacing:-.05em;line-height:17px}
.tl-title span{color:var(--green)}
.tl-sub{font-size:5.4px}
.tl-line{position:absolute;height:1px;background:#b9bec4}
.stop{position:absolute;top:98px;width:70px}
.stop .time{font-size:5.8px}
.stop .pt{position:absolute;top:17px;left:-2px;width:5px;height:5px;border-radius:50%;border:1px solid;background:var(--dark)}
.stop h6{font-size:6px;font-weight:400;line-height:6.6px;margin-top:20px}
.stop p{font-size:3.8px;line-height:5px;margin-top:5px;color:#d7dbe0}
.pgno{position:absolute;right:20px;bottom:12px;font-size:3.4px;color:#c7ccd2}
</style>
</head>
<body>
<div class="canvas">

  <!-- Vision / Mission / Result -->
  <section class="slide s-vmr">
    <div class="ring" style="left:618px;top:-40px;width:200px;height:200px;border:26px solid var(--faint)"></div>
    <h1 class="abs head title">Company Featured</h1>
    <p class="abs sub">Insert Your Creative Idea</p>
    <div class="brand" style="left:590px;top:54px">
      <span class="dot" style="width:34px;height:34px"></span>
      <span class="name" style="font-size:22px">MervoSan</span>
    </div>

    <div class="pillar" style="left:63px">
      <svg viewBox="0 0 40 44"><path d="M16 4c4-4 10-2 10 4 0 4-3 8-6 12L9 40l-5-3 11-18c2-3 4-6 3-9-1-2-3-2-4 0l-3-3z" fill="#7a7a7a"/><path d="M20 22l5-6 13 20-5 4z" fill="#1e73c8"/></svg>
      <div class="bar" style="background:var(--navy)"></div>
      <h3 style="color:var(--navy)">OUR VISION</h3>
      <p>Lorem ipsum dolor sit amet, consectetur adipiscing elit. Nulla imperdiet volutpat dui at fermentum.</p>
    </div>
    <div class="pillar" style="left:299px">
      <svg viewBox="0 0 40 44"><rect x="17" y="2" width="5" height="5" fill="#6a6a6a"/><rect x="15" y="7" width="9" height="16" rx="2" transform="rotate(25 19 15)" fill="#6a6a6a"/><path d="M12 20a10 10 0 0 0 2 19h-3v-2M10 42h22v-3H10z" fill="#6a6a6a"/><rect x="20" y="26" width="10" height="3" fill="#6a6a6a"/><path d="M11 24a9 9 0 0 0 4 15" stroke="#6a6a6a" stroke-width="4" fill="none"/></svg>
      <div class="bar" style="background:var(--green)"></div>
      <h3 style="color:var(--green)">OUR MISSION</h3>
      <p>Lorem ipsum dolor sit amet, consectetur adipiscing elit. Nulla imperdiet volutpat dui at fermentum.</p>
    </div>
    <div class="pillar" style="left:536px">
      <svg viewBox="0 0 40 44"><path d="M20 38C8 30 6 24 8 18c2-5 8-6 12-2 4-4 10-3 12 2 2 6 0 12-12 20z" fill="#6a6a6a"/><path d="M14 16V6l3 0v9M20 14V3h3v11M26 16V6h3v10" stroke="var(--orange)" stroke-width="3" fill="none"/><path d="M12 18c4 2 12 2 16 0l2 6c-6 3-14 3-20 0z" fill="var(--orange)"/></svg>
      <div class="bar" style="background:var(--orange)"></div>
      <h3 style="color:var(--orange)">OUR RESULT</h3>
      <p>Lorem ipsum dolor sit amet, consectetur adipiscing elit. Nulla imperdiet volutpat dui at fermentum.</p>
    </div>

    <div class="vmr-foot footer">
      <div class="url"><span>www.mervosan-site.com</span></div>
      <div class="pg"><span>7</span></div>
    </div>
  </section>

  <!-- Strategy and performance -->
  <section class="slide s-strat">
    <div class="brand" style="left:14px;top:85px">
      <span class="dot" style="width:17px;height:17px"></span>
      <span class="name" style="font-size:11px">MervoSan</span>
    </div>
    <h2 class="abs head t"><span>Talking</span><br>Strategy And<br>Performance</h2>
    <p class="abs sub">Insert Your Creative Idea</p>
    <p class="abs note">Lorem ipsum dolor sit amet, consectetur adipiscing elit. Nulla imperdiet volutpat dui at fermentum. Aliquam erat volutpat.</p>
    <div class="photo" role="img" aria-label="Portrait photo of a doctor holding a clipboard" style="left:148px;top:0;width:104px;height:117px;background:linear-gradient(160deg,#8c8377,#e7e4df 55%,#b9b0a6)"></div>
    <div class="abs card">
      <h4>NORA VALE</h4>
      <p>Lorem ipsum dolor sit amet, consectetur adipiscing elit. Nulla imperdiet volutpat dui at fermentum.</p>
      <p>Lorem ipsum dolor sit amet, consectetur adipiscing elit.</p>
    </div>
    <div class="abs panel">
      <div class="feat" style="top:27px">
        <svg viewBox="0 0 12 14"><path d="M2 1h8v4a4 4 0 0 1-8 0zM5 9h2v3H5zM3 12h6v2H3z" fill="#fff"/></svg>
        <div><h5>AWWARDS</h5><p>Lorem ipsum dolor sit amet, consectetur adipiscing elit Nulla iperdiet volutpat</p></div>
      </div>
      <div class="feat" style="top:77px">
        <svg viewBox="0 0 12 14"><path d="M5 0h3v6H5zM3 6a5 5 0 0 0 3 7H2v1h9v-1H8a4 4 0 0 1-4-7z" fill="#fff"/></svg>
        <div><h5>RESEARCH</h5><p>Lorem ipsum dolor sit amet, consectetur adipiscing elit Nulla iperdiet volutpat</p></div>
      </div>
      <div class="feat" style="top:126px">
        <svg viewBox="0 0 12 14"><path d="M4 0h6v10H8V2H4zM1 3h6v11H1z" fill="#fff"/></svg>
        <div><h5>PAPERS</h5><p>Lorem ipsum dolor sit amet, consectetur adipiscing elit Nulla iperdiet volutpat</p></div>
      </div>
    </div>
  </section>

  <!-- Key figures -->
  <section class="slide s-fig">
    <div class="brand" style="left:163px;top:14px">
      <span class="dot" style="width:17px;height:17px"></span>
      <span class="name" style="font-size:11px">MervoSan</span>
    </div>
    <h2 class="abs head title">Company Featured</h2>
    <p class="abs sub">Insert Your Creative Idea</p>
    <div class="stat" style="left:29px"><div class="box" style="background:var(--navy)"><b>15K</b><small>LOREM IPSUM<br>DOLOR</small></div><p>Lorem ipsum dolor sit amet, consectetur adipiscing elit. Nulla imperdiet volutpat dui at fermentum. Aliquam erat volutpat.</p></div>
    <div class="stat" style="left:99px"><div class="box" style="background:var(--green)"><b>455K</b><small>LOREM IPSUM<br>DOLOR</small></div><p>Lorem ipsum dolor sit amet, consectetur adipiscing elit. Nulla imperdiet volutpat dui at fermentum. Aliquam erat volutpat.</p></div>
    <div class="stat" style="left:169px"><div class="box" style="background:var(--orange)"><b>6455K</b><small>LOREM IPSUM<br>DOLOR</small></div><p>Lorem ipsum dolor sit amet, consectetur adipiscing elit. Nulla imperdiet volutpat dui at fermentum. Aliquam erat volutpat.</p></div>
    <div class="photo" role="img" aria-label="Photo of cinnamon sticks in a clay pot on wood" style="left:251px;top:0;width:105px;height:117px;background:linear-gradient(150deg,#5a4a3e,#8a6a52 50%,#3b2e26)"></div>
    <div class="abs panel">
      <svg class="abs" style="left:12px;top:12px" width="18" height="18" viewBox="0 0 18 18"><path d="M6 1h6v1h-1v5l6 10H1L7 7V2H6z" fill="none" stroke="#fff" stroke-width="1.2"/><path d="M4 11h10l3 6H1z" fill="var(--green)"/></svg>
      <span class="abs big">158000+</span>
      <span class="abs res">Research</span>
      <span class="abs rule"></span>
      <p class="abs ptext">Lorem ipsum dolor sit amet, consectetur adipiscing elit. Nulla imperdiet volutpat dui at fermentum. Aliquam erat volutpat.</p>
    </div>
  </section>

  <!-- What we do -->
  <section class="slide s-do">
    <div class="photo" role="img" aria-label="Photo of cinnamon sticks in a clay pot on a wooden table" style="left:0;top:0;width:377px;height:112px;background:linear-gradient(100deg,#4a3a30,#6d5443 45%,#8a6a55 70%,#4d3c31)"></div>
    <div class="abs box">
      <h2 class="abs head title">What We Do</h2>
      <p class="abs sub">Insert Your Creative Idea</p>
    </div>
    <p class="abs lorem body">Lorem ipsum dolor sit amet, consectetur adipiscing elit. Nulla imperdiet volutpat dui at fermentum. Aliquam erat volutpat. Aenean lacinia lacus aliquet ante mollis, sollicitudin tempor tortor aliquam. Nulla facilisi. Nam auctor metus vitae quam gravida, ac vehicula elit mollis. Nunc elementum fringilla nisl, a ornare arcu condimentum a. Nulla euismod congue arcu quis feugiat. Phasellus porttitor felis mauris, sed suscipit quam egestas nec. Suspendisse sapien quam, cursus et tincidunt quis, ultricies sit amet. third-party research, surveys and studies generally.</p>
    <div class="service" style="left:153px">
      <div class="c" style="background:var(--navy)"><svg viewBox="0 0 16 16"><path d="M11 1l4 4-2 2-1-1-6 6-3 1 1-3 6-6-1-1z" fill="#fff"/><path d="M3 13l-1 2" stroke="#5ab4e8" stroke-width="2"/></svg></div>
      <h6>SUBTITLE HERE</h6><p>Join with us and we'll make the world in our hand. It's using to make your look good and awesome in your audiences view.</p>
    </div>
    <div class="service" style="left:226px">
      <div class="c" style="background:var(--green)"><svg viewBox="0 0 16 16"><path d="M8 7C5 4 3 6 4 8l4 3 4-3c1-2-1-4-4-1z" fill="#ffd23a"/><path d="M1 6c1 5 4 8 7 8s6-3 7-8" stroke="#fff" stroke-width="1.6" fill="none"/></svg></div>
      <h6>SUBTITLE HERE</h6><p>Join with us and we'll make the world in our hand. It's using to make your look good and awesome in your audiences view.</p>
    </div>
    <div class="service" style="left:299px">
      <div class="c" style="background:var(--orange)"><svg viewBox="0 0 16 16"><path d="M0 8h4l2-5 3 10 2-5h5" stroke="#fff" stroke-width="1.6" fill="none"/></svg></div>
      <h6>SUBTITLE HERE</h6><p>Join with us and we'll make the world in our hand. It's using to make your look good and awesome in your audiences view.</p>
    </div>
    <div class="do-foot"><div class="url">www.mervosan-site.com</div><div class="pg">12</div></div>
  </section>

  <!-- Timeline of contents -->
  <section class="slide dark s-time">
    <div class="ring" style="left:310px;top:-30px;width:110px;height:110px;border:14px solid #2a3440"></div>
    <div class="abs" style="left:21px;top:0;width:28px;height:18px;background:var(--green)"></div>
    <h2 class="abs tl-title" style="left:22px;top:36px">TIMELINE OF<br><span>CONTENTS</span></h2>
    <p class="abs tl-sub" style="left:22px;top:72px">Insert Your Creative Idea</p>
    <div class="tl-line" style="left:0;top:118px;width:379px"></div>
    <div class="stop" style="left:96px"><div class="time">07:30</div><span class="pt" style="border-color:#1e73c8;background:#1e73c8"></span><h6>WHO WE<br>ARE?</h6><p>Lorem ipsum dolor sit amet, consectetur adipiscing elit. Nulla imperdiet volutpat dui at fermentum.</p></div>
    <div class="stop" style="left:166px"><div class="time">09:30</div><span class="pt" style="border-color:var(--green)"></span><h6>BEST SERVICE<br>OF US</h6><p>Lorem ipsum dolor sit amet, consectetur adipiscing elit. Nulla imperdiet volutpat dui at fermentum.</p></div>
    <div class="stop" style="left:235px"><div class="time">12:00</div><span class="pt" style="border-color:var(--orange)"></span><h6>VERY USEFUL<br>TIMELINE</h6><p>Lorem ipsum dolor sit amet, consectetur adipiscing elit. Nulla imperdiet volutpat dui at fermentum.</p></div>
    <div class="stop" style="left:304px"><div class="time">15:30</div><span class="pt" style="border-color:var(--red)"></span><h6>GOOD<br>VISION</h6><p>Lorem ipsum dolor sit amet, consectetur adipiscing elit. Nulla imperdiet volutpat dui at fermentum.</p></div>
    <span class="pgno">8</span>
  </section>

  <!-- End of contents -->
  <section class="slide dark s-end">
    <div class="ring" style="left:310px;top:-30px;width:110px;height:110px;border:14px solid #2a3440"></div>
    <div class="tl-line" style="left:0;top:118px;width:277px"></div>
    <div class="tl-line" style="left:277px;top:55px;width:1px;height:64px"></div>
    <h2 class="abs tl-title" style="left:284px;top:60px">END OF<br><span>CONTENTS</span></h2>
    <p class="abs" style="left:285px;top:91px;width:60px;font-size:3.8px;line-height:5px">Lorem ipsum dolor sit amet, consectetur adipiscing elit. Nulla imperdiet volutpat dui at fermentum.</p>
    <div class="stop" style="left:44px"><div class="time">07:30</div><span class="pt" style="border-color:#4ab0e0"></span><h6>WHO WE<br>ARE?</h6><p>Lorem ipsum dolor sit amet, consectetur adipiscing elit. Nulla imperdiet volutpat dui at fermentum.</p></div>
    <div class="stop" style="left:124px"><div class="time">09:30</div><span class="pt" style="border-color:var(--green)"></span><h6>BEST SERVICE<br>OF US</h6><p>Lorem ipsum dolor sit amet, consectetur adipiscing elit. Nulla imperdiet volutpat dui at fermentum.</p></div>
    <div class="stop" style="left:205px"><div class="time">12:00</div><span class="pt" style="border-color:var(--orange)"></span><h6>VERY USEFUL<br>TIMELINE</h6><p>Lorem ipsum dolor sit amet, consectetur adipiscing elit. Nulla imperdiet volutpat dui at fermentum.</p></div>
    <span class="pgno">9</span>
  </section>

</div>
</body>
</html>
```